Dental practice Re-design and relaunch the website while retaining the CI

We need a re-desgin of our totally obsolete and poorly maintained page (it was problematic to make changes). The wish is that we get a contemporary design and above all the site can update itself without much know-how about web techniques have to have. The current website: www.praxis-morlindau.de Pictures are then made available and made available.

Target Market(s)

patient information

Number of Pages Required

1 page

Font styles to use
Sans Serif

Colors

Designer to choose colors to be used in the design.

Requirements
Must have
• An area that we can revitalize ourselves with little effort!
Should not have
• Animations or similar

```html
<!DOCTYPE html>
<html lang="en">
<head>
<meta charset="utf-8">
<title>Dental Practice Morlindau</title>
<link href="https://fonts.googleapis.com/css2?family=Raleway:wght@400;500;600;700;800&family=Roboto+Slab:wght@400;700&display=swap" rel="stylesheet">
<style>
:root{
  --blue:#1aa5e6;
  --navy:#165c8e;
  --navy-dark:#0f4a76;
  --ink:#333;
  --muted:#666;
  --soft:#efefef;
  --white:#fff;
}
*{box-sizing:border-box;margin:0;padding:0}
html,body{width:1200px;height:3303px;overflow:hidden}
body{font-family:"Raleway",sans-serif;color:var(--ink);background:var(--white);position:relative}
.abs{position:absolute}
.slab{font-family:"Roboto Slab",serif}

/* hero */
.hero{left:0;top:0;width:1200px;height:572px;background:linear-gradient(100deg,#9fb3c4 0%,#c6d4df 40%,#e6e2dc 70%,#d9cfc4 100%)}
.hero-photo{left:420px;top:0;width:780px;height:572px;background:radial-gradient(ellipse at 55% 40%,#e9d3c2 0%,#d8c2b0 35%,rgba(200,210,220,0) 70%)}
.brand{left:70px;top:22px;color:var(--white);text-align:center;width:220px}
.brand .dot{width:26px;height:26px;border-radius:50%;background:var(--white);margin:0 auto 8px}
.brand .small{font-size:13px;letter-spacing:1px}
.brand .name{font-size:27px;letter-spacing:1.5px;font-weight:500}
.menu{left:1097px;top:28px;width:32px}
.menu span{display:block;height:3px;background:var(--white);margin-bottom:5px}
.hero-copy{left:84px;top:272px;color:var(--white)}
.hero-copy .welcome{font-size:21px;font-weight:500;letter-spacing:.5px}
.hero-copy .big{font-size:52px;font-weight:800;line-height:1.1;margin-top:6px}
.hero-copy .big em{font-style:normal;color:var(--navy)}
.hero-copy .sub{font-size:30px;font-weight:500}
.hero-copy .sub b{font-weight:800}
.btn{display:inline-block;font-size:11px;font-weight:700;text-transform:uppercase;text-align:center;line-height:37px;height:37px;letter-spacing:.5px}
.btn-solid{background:var(--blue);color:var(--white)}
.btn-line{border:2px solid var(--blue);color:var(--blue);background:var(--white);line-height:33px}

/* info bar */
.info{left:0;top:572px;width:1200px;height:88px;background:var(--navy)}
.info-item{top:20px;display:flex;gap:20px;color:var(--white)}
.info-item svg{flex:none}
.info-item .t{font-family:"Roboto Slab",serif;font-size:14px;font-weight:700;margin-top:2px}
.info-item .s{font-size:13px;color:#7fa8c8;margin-top:10px}

/* intro */
.intro{left:0;top:660px;width:1200px;height:577px;background:linear-gradient(180deg,#e9edf3 0%,#f6f7fa 50%,#e8ecf2 100%)}
.nurse{left:705px;top:40px;width:375px;height:537px;background:linear-gradient(180deg,#3a2b26 0%,#e2c0a8 22%,#67c3d6 45%,#4fb2c9 100%);border-radius:160px 160px 0 0}
.intro h2{left:77px;top:68px;font-size:28px;font-weight:400;color:var(--blue);line-height:1.25;width:520px}
.divider{height:20px}
.divider .line{position:absolute;top:9px;height:1px;background:#bbb;width:100%}
.divider .knob{position:absolute;left:50%;top:2px;width:16px;height:16px;margin-left:-8px;border-radius:50%;background:#999}
.intro p{font-size:13px;line-height:24px;color:#555;width:510px}
.intro p b{color:var(--ink)}
.blue-rule{left:0;top:1236px;width:1200px;height:7px;background:var(--blue)}

/* services */
.services{left:0;top:1243px;width:1200px;height:655px;background:var(--soft)}
.sec-title{font-family:"Roboto Slab",serif;font-size:28px;font-weight:700;color:var(--blue)}
.card{top:184px;width:248px}
.card .img{height:169px}
.card .icon{position:absolute;left:93px;top:138px;width:62px;height:62px;border-radius:50%;background:var(--navy);border:3px solid var(--white);display:flex;align-items:center;justify-content:center}
.card h3{margin-top:72px;font-family:"Roboto Slab",serif;font-size:17px;font-weight:700;text-transform:uppercase;color:var(--ink)}
.card.active h3{color:var(--blue)}
.card p{margin-top:16px;font-size:13px;line-height:22px;color:#555;width:220px}
.arrow{top:310px}

/* reviews */
.reviews{left:0;top:1898px;width:1200px;height:337px;background:var(--navy);overflow:hidden}
.reviews .photo{left:0;top:0;width:1200px;height:337px}
.reviews h2{left:86px;top:130px;font-family:"Roboto Slab",serif;font-size:38px;font-weight:700;color:var(--white)}
.reviews h2 span{color:var(--blue);font-weight:400}
.portrait{left:511px;top:121px;width:101px;height:101px;border:4px solid var(--white);background:linear-gradient(180deg,#3b2c28,#b08a78 60%,#ece9e6)}
.quote{left:660px;top:118px;width:460px;font-size:13px;line-height:29px;color:#dbe7f1}
.quote-name{left:660px;top:236px;font-family:"Roboto Slab",serif;font-weight:700;font-size:17px;color:var(--white)}
.dots{left:838px;top:283px;display:flex;gap:7px}
.dots i{width:11px;height:11px;border-radius:50%;background:var(--white)}
.dots i:first-child{background:var(--blue)}

/* facilities */
.facilities h2{left:86px;top:2345px}
.facilities p{left:103px;top:2452px;width:1000px;font-size:20px;line-height:34px;color:#777}
.tile{width:321px;height:240px}
.tile.hover{background:rgba(26,190,220,.85);color:var(--white);display:flex;flex-direction:column;align-items:center;justify-content:center;gap:14px;font-size:20px;font-weight:500;letter-spacing:.5px}

/* footer */
.footer{left:0;top:3188px;width:1200px;height:115px;background:var(--navy-dark)}
.footer .brand{top:22px;left:52px;width:210px}
.footer .brand .name{font-size:24px}
.footer .copy{left:410px;top:52px;font-size:12px;color:#9fbbd2}
.social{top:36px;display:flex;gap:18px;left:935px}
.social i{width:36px;height:36px;border-radius:50%;background:var(--white);display:block}
</style>
</head>
<body>

<section class="abs hero">
  <div class="abs hero-photo" role="img" aria-label="Smiling senior couple embracing"></div>
  <div class="abs brand">
    <div class="dot"></div>
    <div class="small">ZAHNÄRZTLICHE PRAXIS</div>
    <div class="name">MORLINDAU</div>
  </div>
  <div class="abs menu"><span></span><span></span><span></span></div>
  <div class="abs hero-copy">
    <div class="welcome">WELCOME TO THE PAGES OF THE</div>
    <div class="big">DENTAL <em>PRACTICE</em></div>
    <div class="sub">OF MORLINDAU IN <b>STUTTGART</b></div>
  </div>
  <a class="abs btn btn-solid" style="left:84px;top:440px;width:123px">Know more</a>
</section>

<section class="abs info">
  <div class="abs info-item" style="left:73px">
    <svg width="38" height="38" viewBox="0 0 38 38"><circle cx="19" cy="19" r="16" fill="none" stroke="#fff" stroke-width="3"/><path d="M19 10v9l-6 4" stroke="#fff" stroke-width="3" fill="none"/></svg>
    <div><div class="t">Monday - Friday : 009:00 - 19:00</div><div class="s">Saturday and Sunday - Closed</div></div>
  </div>
  <div class="abs info-item" style="left:495px">
    <svg width="36" height="38" viewBox="0 0 36 38"><path d="M8 3l7 7-4 5c2 5 6 9 11 11l5-4 7 7-4 6C17 35 2 19 2 8z" fill="#fff"/></svg>
    <div><div class="t">+49 (0) 711/40 27 385</div><div class="s">info@praxis-morlindau.de</div></div>
  </div>
  <div class="abs info-item" style="left:836px">
    <svg width="30" height="40" viewBox="0 0 30 40"><path d="M15 1C7 1 2 7 2 14c0 10 13 25 13 25s13-15 13-25C28 7 23 1 15 1z" fill="#fff"/><circle cx="15" cy="14" r="5" fill="#165c8e"/></svg>
    <div><div class="t">Dentistry practice of Morlindau</div><div class="s">Lindenhofweg 12, 70439 Stuttgart</div></div>
  </div>
</section>

<section class="abs intro">
  <div class="abs nurse" role="img" aria-label="Smiling dental nurse holding a folder"></div>
  <h2 class="abs slab">We will do our Best to Give you an Untroubled Laugh.</h2>
  <div class="abs divider" style="left:130px;top:160px;width:250px"><div class="line"></div><div class="knob"></div></div>
  <div class="abs" style="left:77px;top:218px">
    <p>Our focus is full ceramic restorations, microscopic endodontics, periodontics and minimally invasive filling therapy.</p>
    <p style="margin-top:14px">Through our practice laboratory and the Ceravo Lab, we are able to manufacture prosthetics as individually as possible for you. Continuous training of the whole team ensures a state-of-the-art knowledge.</p>
    <p style="margin-top:14px">Stay a while on our pages and find out <b>about us</b> or Should you have any questions regarding certain services, please <b>contact us.</b></p>
  </div>
  <a class="abs btn btn-line" style="left:88px;top:480px;width:117px">Know more</a>
  <a class="abs btn btn-solid" style="left:218px;top:480px;width:119px">Contact us</a>
</section>
<div class="abs blue-rule"></div>

<section class="abs services">
  <h2 class="abs sec-title" style="left:86px;top:70px">Our Services</h2>
  <div class="abs divider" style="left:66px;top:116px;width:226px"><div class="line"></div><div class="knob"></div></div>

  <svg class="abs arrow" style="left:12px" width="28" height="64" viewBox="0 0 28 64"><path d="M24 2L4 32l20 30" fill="none" stroke="#8bbcd6" stroke-width="2"/></svg>
  <svg class="abs arrow" style="left:1158px" width="28" height="64" viewBox="0 0 28 64"><path d="M4 2l20 30L4 62" fill="none" stroke="#1aa5e6" stroke-width="2"/></svg>

  <div class="abs card active" style="left:62px">
    <div class="img" role="img" aria-label="Smiling child in a dental chair" style="background:linear-gradient(135deg,#f0c9a3,#d9a77e 60%,#e8e2da)"></div>
    <div class="icon"><svg width="30" height="30" viewBox="0 0 30 30"><circle cx="15" cy="15" r="12" fill="none" stroke="#fff" stroke-width="2"/><path d="M9 17c3 4 9 4 12 0" stroke="#fff" stroke-width="2" fill="none"/><circle cx="11" cy="12" r="1.5" fill="#fff"/><circle cx="19" cy="12" r="1.5" fill="#fff"/></svg></div>
    <h3>Dental Services</h3>
    <p>Lorem ipsum dolor sit amet, consectetur adipiscing elit. Maecenas sagittis mi faucibus risus auctor scelerisque.</p>
  </div>
  <div class="abs card" style="left:337px">
    <div class="img" role="img" aria-label="Dental implant model" style="background:linear-gradient(135deg,#8fd7ef,#3fb6e0 60%,#bfe9f6)"></div>
    <div class="icon"><svg width="26" height="30" viewBox="0 0 26 30"><path d="M6 2c-5 0-5 8-3 13 1 4 2 13 5 13s3-8 5-8 2 8 5 8 4-9 5-13c2-5 2-13-3-13-4 0-5 2-7 2S10 2 6 2z" fill="none" stroke="#fff" stroke-width="2"/></svg></div>
    <h3>Implants</h3>
    <p>Praesent porta lacus a viverra tempus. Proin maximus felis ac risus aliquam maximus. Pellentesque quis orci tempus.</p>
  </div>
  <div class="abs card" style="left:612px">
    <div class="img" role="img" aria-label="Patient receiving a dental examination" style="background:linear-gradient(135deg,#e8e4e0,#c9b6a6 50%,#5c6c78)"></div>
    <div class="icon"><svg width="28" height="30" viewBox="0 0 28 30"><circle cx="15" cy="11" r="8" fill="none" stroke="#fff" stroke-width="2"/><path d="M9 17L3 27" stroke="#fff" stroke-width="3"/></svg></div>
    <h3>Dentistry</h3>
    <p>Vestibulum ante ipsum primis in faucibus orci luctus et ultrices posuere cubilia Curae; Morbi a pulvinar leo.</p>
  </div>
  <div class="abs card" style="left:887px">
    <div class="img" role="img" aria-label="Smile with dental braces" style="background:linear-gradient(180deg,#f3ece6,#d9525e 40%,#e9e2dd 55%,#d24a57 75%,#f3ece6)"></div>
    <div class="icon"><svg width="30" height="28" viewBox="0 0 30 28"><rect x="4" y="8" width="22" height="12" rx="3" fill="none" stroke="#fff" stroke-width="2"/><path d="M4 14h22M11 8v12M19 8v12" stroke="#fff" stroke-width="2"/></svg></div>
    <h3>Clear Aligners</h3>
    <p>Nullam eleifend lectus a tortor interdum, non sodales ante vehicula. Proin consequat, at commodo.</p>
  </div>
</section>

<section class="abs reviews">
  <svg class="abs photo" width="1200" height="337" viewBox="0 0 1200 337" role="img" aria-label="Hands typing on a laptop keyboard">
    <defs><linearGradient id="g" x1="0" y1="0" x2="1" y2="1"><stop offset="0" stop-color="#6a6a6a"/><stop offset="1" stop-color="#2e2e2e"/></linearGradient></defs>
    <polygon points="0,0 506,0 458,337 0,337" fill="url(#g)"/>
    <polygon points="506,0 520,0 472,337 458,337" fill="#1aa5e6"/>
  </svg>
  <h2 class="abs"><span>Client</span> REVIEWS</h2>
  <div class="abs divider" style="left:220px;top:190px;width:30px"><div class="knob" style="background:#fff"></div></div>
  <div class="abs portrait" role="img" aria-label="Portrait of reviewing patient"></div>
  <svg class="abs" style="left:634px;top:114px" width="18" height="16" viewBox="0 0 18 16"><path d="M0 16V8L4 0h3L5 8h3v8zM10 16V8l4-8h3l-2 8h3v8z" fill="#5b8db3"/></svg>
  <p class="abs quote">Quisque posuere rhoncus erat, sit amet aliquet augue. Donec eros massa, gravida ac lectus et, pharetra interdum lectus. Sed vel scelerisque quam, id fringilla ante. Vivamus sagittis velit quis dictum ultricies. Nullam eleifend lectus a tortor interdum, non sodales.</p>
  <div class="abs quote-name">MARA ELLISON</div>
  <div class="abs dots"><i></i><i></i><i></i></div>
</section>

<section class="facilities">
  <h2 class="abs sec-title">Treatment Facilities</h2>
  <div class="abs divider" style="left:84px;top:2396px;width:226px"><div class="line"></div><div class="knob"></div></div>
  <p class="abs">We offer our patients highly modern treatment rooms. The latest technologies and procedures guarantee optimal dental treatment in our practice.</p>

  <div class="abs tile" style="left:110px;top:2558px;background:linear-gradient(135deg,#6f8f7a,#2f5a46)" role="img" aria-label="Reception area">
    <div class="tile hover" style="position:absolute;inset:0">
      <svg width="44" height="44" viewBox="0 0 44 44"><circle cx="18" cy="18" r="13" fill="none" stroke="#fff" stroke-width="5"/><path d="M28 28l12 12" stroke="#fff" stroke-width="6"/></svg>
      <span>RECEPTION AREA</span>
    </div>
  </div>
  <div class="abs tile" style="left:441px;top:2558px;background:linear-gradient(135deg,#efe9e2,#b9a696 55%,#c23a3a 85%)" role="img" aria-label="Consultation room with red chairs"></div>
  <div class="abs tile" style="left:773px;top:2558px;background:linear-gradient(135deg,#f1efe8,#d8d3bd 60%,#a9b3a0)" role="img" aria-label="Bright waiting room with sofa"></div>
  <div class="abs tile" style="left:110px;top:2812px;background:linear-gradient(135deg,#c9b9a8,#e8e2dc 50%,#8c7a6e)" role="img" aria-label="Treatment room with dental chair"></div>
  <div class="abs tile" style="left:441px;top:2812px;background:linear-gradient(135deg,#d9d1c3,#8a7c6a 55%,#3f4a52)" role="img" aria-label="Dental laboratory workplace"></div>
  <div class="abs tile" style="left:773px;top:2812px;background:linear-gradient(135deg,#f5f5f5,#e2e2e2 60%,#c9c9c9)" role="img" aria-label="Decorative wall clock"></div>

  <a class="abs btn btn-solid" style="left:465px;top:3109px;width:268px;height:35px;line-height:35px">Click here for complete gallery</a>
</section>

<footer class="abs footer">
  <div class="abs brand">
    <div class="dot" style="width:20px;height:20px"></div>
    <div class="small" style="font-size:11px">ZAHNÄRZTLICHE PRAXIS</div>
    <div class="name">MORLINDAU</div>
  </div>
  <div class="abs copy">© Copyrights 2017 Zahnarztliche Praxis. All Rights Reserved</div>
  <div class="abs social"><i></i><i></i><i></i><i></i></div>
</footer>

</body>
</html>
```